Webdesign mit Wordpress DIVI Theme - CI und Logo vorhanden
Zielgruppe
Wir veranstalten eine Messe zum Thema Reinigung von Zügen und Straßenbahnen. Die Webseite soll folgende Zielgruppen ansprechen:
* Aussteller (Reinigungsindustrie)
* Besucher
* Presse
Aufgabenstellung
Wir brauchen ein Wordpress Deisgn basierend auf dem DIVI Theme!
Erwartet wird ein fertiges Layout mit Divi gemacht, welches wir importieren können.
Es gibt bereits einen Styleguide und ein Logo. Diese sind angehängt. Bitte entsprechend berücksichtigen.

```html
<!DOCTYPE html>
<html lang="de">
<head>
<meta charset="utf-8">
<title>purerail – Messe</title>
<link href="https://fonts.googleapis.com/css2?family=Montserrat:wght@300;400;500;600;700&display=swap" rel="stylesheet">
<style>
:root{
  --yellow:#ffcc00;
  --sky:#80c4d7;
  --sky-light:#cfe9f1;
  --teal:#2f5567;
  --ink:#2f5567;
  --text:#5a5a5a;
  --grey-band:#eef0f2;
  --night:#0d1a26;
  --white:#ffffff;
}
*{box-sizing:border-box;margin:0;padding:0}
html,body{width:1200px;height:4856px;overflow:hidden}
body{position:relative;font-family:"Montserrat",Arial,sans-serif;color:var(--text);background:var(--white)}
.abs{position:absolute}
p{font-size:15.5px;line-height:20px;font-weight:400}
h2.section-title{position:absolute;left:151px;font-size:32px;font-weight:600;color:var(--ink)}
h2.section-title.yellow{color:var(--yellow)}
.section-text{position:absolute;left:151px;width:900px;color:var(--text)}
.on-dark{color:#e6eef2}

/* hero */
.hero-photo{left:0;top:0;width:1200px;height:690px;background:radial-gradient(ellipse at 55% 25%,#6f8ea6 0%,#2c4257 28%,#0e1b28 60%,#060c12 100%)}
.hero-track{left:0;top:0;width:1200px;height:690px;background:linear-gradient(160deg,transparent 45%,rgba(255,200,40,.35) 62%,transparent 72%)}
.top-nav{right:80px;top:30px;display:flex;gap:34px;font-size:12px;font-weight:600;color:#fff}
.brand{left:151px;top:60px;display:flex;align-items:center;gap:12px;color:#fff;font-size:40px;font-weight:600}
.brand-dot{width:26px;height:26px;border-radius:50%;background:var(--sky)}
.event-tag{left:324px;top:84px;width:200px;height:62px;border-left:2px solid var(--yellow);border-top:2px solid var(--yellow);padding:8px 0 0 14px;color:#fff}
.event-tag:after{content:"";position:absolute;right:0;bottom:0;width:12px;height:12px;border-right:2px solid var(--yellow);border-bottom:2px solid var(--yellow)}
.event-tag .name{font-size:25px;font-weight:300;line-height:28px}
.event-tag .date{font-size:14px;font-weight:600}
.btn-program{left:891px;top:94px;width:158px;height:42px;display:flex;background:var(--yellow);color:#fff;font-size:12px;font-weight:700}
.btn-program span{flex:1;display:flex;align-items:center;justify-content:center}
.btn-program i{width:38px;border-left:1px solid rgba(255,255,255,.6);display:flex;align-items:center;justify-content:center}
.hero-headline{left:151px;top:300px;font-size:34px;font-weight:700;color:var(--yellow)}
.hero-text{left:151px;top:343px;width:470px;color:#fff;font-size:15.5px}

.tile{position:absolute;background:var(--sky);color:#fff;padding:18px 14px 0}
.tile h3{font-size:32px;font-weight:600;color:var(--ink);line-height:34px;margin-bottom:8px}
.tile p{font-size:14.5px;line-height:19px;color:#e9f5f8}
.tile .chev{position:absolute;left:50%;bottom:10px;margin-left:-10px}
.hero-tile{top:428px;width:290px;height:186px;background:rgba(128,196,215,.88)}

/* about */
.about-bg{left:0;top:670px;width:1200px;height:610px;background:linear-gradient(100deg,#e8ebee 0%,#fafafa 40%,#fff 60%,#eceff1 100%)}
.about-date{left:151px;top:898px;font-size:28px;font-weight:700;color:var(--yellow)}
.about-hours{left:151px;top:950px;font-size:19px;line-height:25px;color:#444}
.about-small{left:151px;width:270px;font-size:14px;line-height:22px}
.video-slot{left:441px;top:897px;width:599px;height:339px;background:linear-gradient(135deg,#1b2a33,#24584d 45%,#132026);}
.video-slot span{position:absolute;right:14px;top:14px;color:#e6e6e6;font-size:14px}

/* visitors */
.teal-band{left:0;background:var(--teal)}
.cta{position:absolute;left:365px;width:451px;background:var(--yellow);text-align:center;color:var(--ink)}
.cta .brandline{font-size:33px;font-weight:300;line-height:40px;padding-top:16px}
.cta .date{font-size:29px;font-weight:600;color:#fff;line-height:34px}
.cta .link{font-size:21px;font-weight:700;margin-top:8px}

/* exhibitors */
.search{position:absolute;left:418px;width:381px;height:38px;border-bottom:1px solid #999;display:flex;align-items:center;gap:18px;padding-left:44px;font-size:21px;font-weight:600;color:#b7c2c9}
.grey-band{left:0;top:2167px;width:1200px;height:620px;background:var(--grey-band)}
.exhibitor{position:absolute;width:169px;height:157px;background:#fff}
.exhibitor .logo{height:114px;display:flex;flex-direction:column;align-items:center;justify-content:center;gap:10px;font-size:17px;color:#555}
.exhibitor .ring{width:40px;height:40px;border:1.5px solid #777;border-radius:50%}
.exhibitor .label{height:43px;background:var(--yellow);color:#fff;font-size:12px;font-weight:700;line-height:15px;text-align:center;padding-top:7px}
.exhibitor.hover .logo{background:#ffe9a8;gap:2px}
.exhibitor.hover .logo b{font-weight:700}
.exhibitor.hover .logo small{font-size:13px;color:#777}
.exhibitor.hover .logo em{font-style:normal;font-size:13px;color:#f2c87a}

/* press */
.press-photo{left:0;top:3024px;width:1200px;height:320px;background:radial-gradient(ellipse at 30% 80%,#1a9ed0 0%,#0b5f8a 35%,#062a40 75%,#031826 100%)}
.press-card{position:absolute;top:3470px;width:290px;height:373px;background:#eff1f2}
.press-card .img{height:185px}
.press-card .date{padding:12px 14px 0;font-size:34px;font-weight:600;color:var(--ink)}
.press-card p{padding:6px 14px 0;font-size:15.5px;line-height:20px;color:#555}

/* contact */
.contact-box{left:151px;top:3937px;width:898px;height:405px;background:var(--sky)}
.contact-box h3{position:absolute;left:0;width:100%;top:42px;text-align:center;font-size:32px;font-weight:300;color:var(--ink)}
.field{position:absolute;background:var(--sky-light);color:#9dbfcc;font-size:14px;padding:8px 8px}
.send{position:absolute;right:48px;top:362px;font-size:24px;font-weight:700;color:var(--ink);display:flex;align-items:center;gap:14px}
.info{position:absolute;top:4371px;text-align:center;color:#dfe9ee}
.info h4{font-size:28px;font-weight:700;color:var(--yellow);line-height:36px}
.info div{font-size:19px}
.map{left:0;top:4474px;width:1200px;height:274px;background:linear-gradient(90deg,#4a4a4a,#3a3b3d 50%,#444)}
.footer{left:0;top:4748px;width:1200px;height:108px;background:var(--teal);color:#e4edf1;font-size:19px}
.footer .left{position:absolute;left:151px;top:44px}
.footer .right{position:absolute;right:151px;top:44px;color:#8aa7b4}
</style>
</head>
<body>

<!-- hero -->
<div class="abs hero-photo" role="img" aria-label="Foto: U-Bahn-Bahnsteig bei Nacht mit einfahrendem Zug und gelber Sicherheitslinie"></div>
<div class="abs hero-track"></div>
<nav class="abs top-nav"><span>Aussteller</span><span>Besucher</span><span>Presse</span></nav>
<div class="abs brand"><span class="brand-dot"></span>purerail</div>
<div class="abs event-tag"><div class="name">Messe Name</div><div class="date">22. bis 25. März 2019</div></div>
<div class="abs btn-program"><span>PROGRAMM</span><i><svg width="10" height="16" viewBox="0 0 10 16"><path d="M2 2l6 6-6 6" stroke="#fff" stroke-width="2" fill="none"/></svg></i></div>
<h1 class="abs hero-headline">Headline</h1>
<p class="abs hero-text">Lorem ipsum dolor sit amet, consectetuer adipiscing elit. Aenean commodo ligula eget dolor. Aenean massa. Cum sociis natoque penatibus et magnis dis parturient</p>

<div class="tile hero-tile" style="left:151px"><h3>Besucher</h3><p>Lorem ipsum dolor sit amet, consectetuer adipiscing elit. Aenean commodo ligula eget dolor. Aenean massa. Cum sociis</p><svg class="chev" width="20" height="12" viewBox="0 0 20 12"><path d="M2 2l8 8 8-8" stroke="#2f5567" stroke-width="2" fill="none"/></svg></div>
<div class="tile hero-tile" style="left:454px"><h3>Aussteller</h3><p>Lorem ipsum dolor sit amet, consectetuer adipiscing elit. Aenean commodo ligula eget dolor. Aenean massa. Cum sociis</p><svg class="chev" width="20" height="12" viewBox="0 0 20 12"><path d="M2 2l8 8 8-8" stroke="#2f5567" stroke-width="2" fill="none"/></svg></div>
<div class="tile hero-tile" style="left:759px"><h3>Presse</h3><p>Lorem ipsum dolor sit amet, consectetuer adipiscing elit. Aenean commodo ligula eget dolor. Aenean massa. Cum sociis</p><svg class="chev" width="20" height="12" viewBox="0 0 20 12"><path d="M2 2l8 8 8-8" stroke="#2f5567" stroke-width="2" fill="none"/></svg></div>

<!-- about -->
<div class="abs about-bg" role="img" aria-label="Heller Hintergrund mit Schaumstruktur"></div>
<svg class="abs" style="left:0;top:630px" width="1200" height="80" viewBox="0 0 1200 80"><path d="M0 40 C400 0 800 50 1200 10 L1200 30 C800 70 400 22 0 62 Z" fill="var(--yellow)"/><path d="M0 62 C400 22 800 70 1200 30 L1200 80 L0 80 Z" fill="#edf0f2"/></svg>
<h2 class="section-title" style="top:728px">Über unsere Messe</h2>
<p class="section-text" style="top:777px">Lorem ipsum dolor sit amet, consectetuer adipiscing elit. Aenean commodo ligula eget dolor. Aenean massa. Cum sociis natoque penatibus et magnis dis parturient. Montes, nascetur ridiculus mus. Donec quam felis, ultricies nec, pellentesque eu, pretium quis, sem. Nulla consequat massa quis enim. Donec pede justo, fringilla vel, aliquet nec, vulputate eget, arcu. Ut quaestemque commodita eture explab is ius.</p>
<div class="abs about-date">22.–25. März 2019</div>
<div class="abs about-hours">Freitag–Montag<br>10.00 bis 18.00 Uhr</div>
<div class="abs about-small" style="top:1026px">Beschreibung<br>Ort und Parken<br>Tickets etc.</div>
<div class="abs about-small" style="top:1116px">Is porepuda nonsectotas et, et quiam que consect orescie nihita quoestiis rae volessint.</div>
<div class="abs video-slot" role="img" aria-label="Videoplatz: U-Bahn fährt in beleuchtete Station ein"><span>evt. Video einfügen?</span></div>

<!-- visitors -->
<svg class="abs" style="left:0;top:1222px" width="1200" height="70" viewBox="0 0 1200 70"><path d="M0 20 C300 60 700 70 1200 0 L1200 70 L0 70 Z" fill="var(--teal)"/></svg>
<div class="abs teal-band" style="top:1290px;width:1200px;height:528px"></div>
<h2 class="section-title yellow" style="top:1334px">Für unsere Besucher</h2>
<p class="section-text on-dark" style="top:1382px">Lorem ipsum dolor sit amet, consectetuer adipiscing elit. Aenean commodo ligula eget dolor. Aenean massa. Cum sociis natoque penatibus et magnis dis parturient. Montes, nascetur ridiculus mus. Donec quam felis, ultricies nec, pellentesque eu, pretium quis, sem. Nulla consequat massa quis enim. Donec pede justo, fringilla vel, aliquet nec, vulputate eget, arcu. Ut quaestemque commodita eture explab is ius.</p>
<div class="tile" style="left:151px;top:1500px;width:290px;height:186px"><h3>Geländeplan</h3><p>Plan als PDF, wo alles ist. ipsum dolor sit amet, consectetuer adipiscing elit. Aenean commodo ligula eget dolor. Aenean mas-</p></div>
<div class="tile" style="left:454px;top:1500px;width:290px;height:186px"><h3>Programm</h3><p>Auszüge aus dem Programm, Vorträge, get2gether etc. Lorem ipsum dolor sit amet, consectetuer adipiscing elit. Aene-</p></div>
<div class="tile" style="left:759px;top:1500px;width:290px;height:186px"><h3>Aufenthalt</h3><p>Parkplätze, Hotels, Verpflegung. Lorem ipsum dolor sit amet, consectetuer adipiscing elit. Aenean commodo ligula eget do-</p></div>
<div class="cta" style="top:1745px;height:145px"><div class="brandline">purerail</div><div class="date">22.–25. März 2019</div><div class="link">Hier geht es zum Kongressprogramm ›</div></div>

<!-- exhibitors -->
<h2 class="section-title" style="top:1951px">Aussteller</h2>
<p class="section-text" style="top:1998px">Lorem ipsum dolor sit amet, consectetuer adipiscing elit. Aenean commodo ligula eget dolor. Aenean massa. Cum sociis natoque penatibus et magnis dis parturient. Montes, nascetur ridiculus mus. Donec quam felis, ultricies nec, pellentesque eu, pretium quis, sem. Nulla consequat massa quis enim. Donec pede justo, fringilla</p>
<div class="search" style="top:2098px"><svg class="abs" style="left:6px;top:6px" width="26" height="26" viewBox="0 0 26 26"><circle cx="11" cy="11" r="8" stroke="#777" stroke-width="2" fill="none"/><path d="M17 17l7 7" stroke="#777" stroke-width="2"/></svg>Ausstellersuche</div>
<div class="abs grey-band"></div>

<div class="exhibitor" style="left:151px;top:2197px"><div class="logo"><span class="ring"></span>Markenlogo</div><div class="label">Firmenname<br>ausgeschrieben</div></div>
<div class="exhibitor" style="left:333px;top:2197px"><div class="logo"><span class="ring"></span>Markenlogo</div><div class="label">Firmenname<br>ausgeschrieben</div></div>
<div class="exhibitor" style="left:514px;top:2197px"><div class="logo"><span class="ring"></span>Markenlogo</div><div class="label">Firmenname<br>ausgeschrieben</div></div>
<div class="exhibitor" style="left:697px;top:2197px"><div class="logo"><span class="ring"></span>Markenlogo</div><div class="label">Firmenname<br>ausgeschrieben</div></div>
<div class="exhibitor" style="left:880px;top:2197px"><div class="logo"><span class="ring"></span>Markenlogo</div><div class="label">Firmenname<br>ausgeschrieben</div></div>

<div class="exhibitor" style="left:151px;top:2380px"><div class="logo"><span class="ring"></span>Markenlogo</div><div class="label">Firmenname<br>ausgeschrieben</div></div>
<div class="exhibitor hover" style="left:333px;top:2380px"><div class="logo"><span>Stand Nr. <b>2124</b></span><small>www.standseite.de</small><em>(Hover Effekt)</em></div><div class="label">Firmenname<br>ausgeschrieben</div></div>
<div class="exhibitor" style="left:514px;top:2380px"><div class="logo"><span class="ring"></span>Markenlogo</div><div class="label">Firmenname<br>ausgeschrieben</div></div>
<div class="exhibitor" style="left:697px;top:2380px"><div class="logo"><span class="ring"></span>Markenlogo</div><div class="label">Firmenname<br>ausgeschrieben</div></div>
<div class="exhibitor" style="left:880px;top:2380px"><div class="logo"><span class="ring"></span>Markenlogo</div><div class="label">Firmenname<br>ausgeschrieben</div></div>

<div class="exhibitor" style="left:151px;top:2562px"><div class="logo"><span class="ring"></span>Markenlogo</div><div class="label">Firmenname<br>ausgeschrieben</div></div>
<div class="exhibitor" style="left:333px;top:2562px"><div class="logo"><span class="ring"></span>Markenlogo</div><div class="label">Firmenname<br>ausgeschrieben</div></div>
<div class="exhibitor" style="left:514px;top:2562px"><div class="logo"><span class="ring"></span>Markenlogo</div><div class="label">Firmenname<br>ausgeschrieben</div></div>
<div class="exhibitor" style="left:697px;top:2562px"><div class="logo"><span class="ring"></span>Markenlogo</div><div class="label">Firmenname<br>ausgeschrieben</div></div>
<div class="exhibitor" style="left:880px;top:2562px"><div class="logo"><span class="ring"></span>Markenlogo</div><div class="label">Firmenname<br>ausgeschrieben</div></div>

<!-- press -->
<svg class="abs" style="left:0;top:2752px" width="1200" height="60" viewBox="0 0 1200 60"><path d="M0 0 C400 40 800 40 1200 20 L1200 60 L0 60 Z" fill="var(--teal)"/></svg>
<div class="abs teal-band" style="top:2810px;width:1200px;height:214px"></div>
<h2 class="section-title yellow" style="top:2864px">Presse</h2>
<p class="section-text on-dark" style="top:2912px">Lorem ipsum dolor sit amet, consectetuer adipiscing elit. Aenean commodo ligula eget dolor. Aenean massa. Cum sociis natoque penatibus et magnis dis parturient. Montes, nascetur ridiculus mus. Donec quam felis, ultricies nec, pellentesque eu, pretium quis, sem. Nulla consequat massa quis enim. Donec pede justo, fringilla</p>
<div class="abs press-photo" role="img" aria-label="Nahaufnahme: blaue Wassertropfen auf einer Oberfläche"></div>
<div class="cta" style="top:3024px;height:141px"><div class="brandline">purerail</div><div class="date">22.–25. März 2019</div><div class="link">Presseakkreditierung ›</div></div>

<div class="search" style="top:3392px"><svg class="abs" style="left:16px;top:6px" width="26" height="26" viewBox="0 0 26 26"><circle cx="11" cy="11" r="8" stroke="#777" stroke-width="2" fill="none"/><path d="M17 17l7 7" stroke="#777" stroke-width="2"/></svg><span style="padding-left:30px">In Presseartikeln suchen</span></div>

<div class="press-card" style="left:151px"><div class="img" role="img" aria-label="Foto: Bahnsteig mit wartender Person und vorbeifahrendem Zug" style="background:linear-gradient(180deg,#5d6770,#2b3238)"></div><div class="date">19/03/01</div><p>Letzte Pressemitteilung, wo alles ist. ipsum dolor sit amet, consectetuer adipiscing elit. Aenean commodo ligula eget dolor. Aenean mastibus et magnis</p></div>
<div class="press-card" style="left:454px"><div class="img" role="img" aria-label="Foto: Bahnsteigkante mit gelber Linie und Lichtspuren" style="background:linear-gradient(180deg,#3c5466,#1a2630 70%,#6b5a1c)"></div><div class="date">19/02/07</div><p>Letzte Pressemitteilung, wo alles ist. ipsum dolor sit amet, consectetuer adipiscing elit. Aenean commodo ligula eget dolor. Aenean mastibus et magnis</p></div>
<div class="press-card" style="left:759px"><div class="img" role="img" aria-label="Foto: U-Bahn in einer Station" style="background:linear-gradient(135deg,#1b2a33,#24584d 50%,#1a2a2e)"></div><div class="date">19/01/31</div><p>Letzte Pressemitteilung, wo alles ist. ipsum dolor sit amet, consectetuer adipiscing elit. Aenean commodo ligula eget dolor. Aenean mastibus et magnis</p></div>

<!-- contact -->
<div class="abs teal-band" style="top:4013px;width:1200px;height:461px"></div>
<div class="abs contact-box">
  <h3>Schreiben Sie uns eine Nachricht</h3>
  <div class="field" style="left:65px;top:108px;width:375px;height:56px">Name</div>
  <div class="field" style="left:456px;top:108px;width:397px;height:56px">E-Mail Adresse</div>
  <div class="field" style="left:65px;top:184px;width:788px;height:154px">Ihre Nachricht an uns</div>
  <div class="send">SENDEN <svg width="14" height="24" viewBox="0 0 14 24"><path d="M2 2l10 10-10 10" stroke="#2f5567" stroke-width="2.5" fill="none"/></svg></div>
</div>
<div class="info" style="left:151px;width:300px"><h4>Telefon</h4><div>0123 | 4567890</div></div>
<div class="info" style="left:450px;width:300px"><h4>Geschäftszeiten</h4><div>täglich von 8.00–16.00 Uhr</div></div>
<div class="info" style="left:770px;width:300px"><h4>Adresse</h4><div>Adresse, Stadt, PLZ, Straße</div></div>
<div class="abs map" role="img" aria-label="Karte mit Standort der Messe"></div>

<footer class="abs footer"><div class="left">Footerleiste Menü und Datenschutz | Impressum</div><div class="right">Social Media Icons?</div></footer>

</body>
</html>
```